Personal Training

The name of my company is Heron Vitality. I am looking for a design that will feature the 8 components I am utilizing in my workouts (strength, flexibility, agility, core, power, balance, cardiovacular, speed) and represent the spider. It is not essesstial to have a spider for my logo but would be nice. If a spider is used please do not use a logo like Crowlord, a tarantula, or anything scary involving a spider (I have female clients who would get scared) lol
If you need me to provide more information please let me know. Feel free to check my website for ideas but ignore the pictures on my site as those are not pictures of me or clients
Thank you in advance!

Industry/Entity Type

Fitness

Contact Information for Business Card

Dale Presky
Company Name: Heron Vitality
Tag line: 8 components to a better you
Website: hervit7.example
Email: dale@hervit7.example
Cell: 555-413-2086

KPTB Certified Personal Trainer
CPR AED Northern Pulse Council
B.A. Exercise Physiology W.L.M., 2004

```html
<!DOCTYPE html>
<html lang="en">
<head>
<meta charset="utf-8">
<title>Heron Vitality – Business Card</title>
<link rel="stylesheet" href="https://fonts.googleapis.com/css2?family=Roboto:wght@300;400;700&family=Roboto+Condensed:wght@700&display=swap">
<style>
  :root {
    --page: #eceaea;
    --card-dark: #232325;
    --card-mid: #303033;
    --accent: #e0484b;
    --accent-deep: #c8282d;
    --accent-soft: #e26363;
    --ink-light: #ffffff;
    --divider: #6b4a4a;
  }
  * { margin: 0; padding: 0; box-sizing: border-box; }
  html, body {
    width: 1200px; height: 900px; overflow: hidden;
    background: var(--page);
  }
  .business-card {
    position: absolute; left: 100px; top: 165px;
    width: 1000px; height: 570px;
    background: radial-gradient(ellipse at 65% 35%, var(--card-mid) 0%, var(--card-dark) 75%);
    overflow: hidden;
    box-shadow: 0 10px 30px rgba(0,0,0,.25);
  }
  .bottom-band {
    position: absolute; left: 0; bottom: 0;
    width: 100%; height: 14px;
    background: var(--accent-deep);
  }
  .web-decoration {
    position: absolute; left: 40px; top: 30px;
    width: 400px; height: 400px; border-radius: 50%;
    background: radial-gradient(circle, rgba(120,80,80,.35) 0%, rgba(90,60,60,.18) 55%, rgba(35,35,37,0) 72%);
  }
  .brand {
    position: absolute; left: 40px; top: 130px; width: 400px;
    text-align: center;
  }
  .brand-dot {
    width: 104px; height: 104px; border-radius: 50%;
    background: var(--accent-soft);
    margin: 0 auto 12px;
  }
  .brand-name {
    font-family: "Roboto", sans-serif; font-weight: 300;
    font-size: 50px; line-height: 1; color: var(--ink-light);
    letter-spacing: -0.5px;
  }
  .tagline {
    font-family: "Roboto", sans-serif; font-weight: 300;
    font-size: 21px; color: var(--ink-light); margin-top: 6px;
  }
  .divider {
    position: absolute; left: 490px; top: 95px;
    width: 2px; height: 420px;
    background: linear-gradient(to bottom, rgba(107,74,74,0), var(--divider) 20%, var(--divider) 80%, rgba(107,74,74,0));
  }
  .contact-block {
    position: absolute; left: 560px; top: 70px; width: 380px;
  }
  .person-name {
    font-family: "Roboto", sans-serif; font-weight: 700;
    font-size: 50px; color: var(--accent); text-align: right; line-height: 1;
  }
  .person-role {
    font-family: "Roboto", sans-serif; font-weight: 700;
    font-size: 20px; color: var(--ink-light); text-align: right;
    letter-spacing: 1px; margin-top: 4px;
  }
  .info-list { list-style: none; margin-top: 22px; }
  .info-item {
    display: flex; align-items: center; gap: 22px;
    font-family: "Roboto Condensed", sans-serif; font-weight: 700;
    color: var(--ink-light); font-size: 24px; height: 42px;
  }
  .info-icon { width: 30px; height: 30px; flex: none; }
  .credentials { margin-top: 14px; }
  .credentials .info-item { font-size: 22px; height: 38px; gap: 18px; }
  .cert-badge { width: 34px; height: 18px; background: var(--accent-deep); border-radius: 3px; flex: none; }
  .cert-badge.round { width: 22px; height: 22px; border-radius: 50%; margin: 0 6px; }
  .website-tab {
    position: absolute; right: 0; bottom: 0;
    width: 330px; height: 58px;
    background: var(--accent-deep);
    border-top-left-radius: 14px;
    font-family: "Roboto", sans-serif; font-weight: 700;
    color: var(--ink-light); font-size: 22px; letter-spacing: 5px;
    display: flex; align-items: center; justify-content: center;
  }
</style>
</head>
<body>
  <div class="business-card">
    <div class="web-decoration" role="img" aria-label="Faint spider web pattern behind the brand name"></div>
    <div class="bottom-band"></div>

    <div class="brand">
      <div class="brand-dot"></div>
      <div class="brand-name">Heron Vitality</div>
      <div class="tagline">8 components to a better you</div>
    </div>

    <div class="divider"></div>

    <div class="contact-block">
      <div class="person-name">Dale Presky</div>
      <div class="person-role">FOUNDER</div>

      <ul class="info-list">
        <li class="info-item">
          <svg class="info-icon" viewBox="0 0 30 30" fill="none" stroke="#e0484b" stroke-width="2">
            <rect x="9" y="3" width="12" height="24" rx="2"/><line x1="13" y1="23" x2="17" y2="23"/>
          </svg>
          555-413-2086
        </li>
        <li class="info-item">
          <svg class="info-icon" viewBox="0 0 30 30" fill="none" stroke="#e0484b" stroke-width="2">
            <rect x="3" y="7" width="24" height="16"/><polyline points="3,7 15,17 27,7"/><line x1="3" y1="23" x2="12" y2="14"/><line x1="27" y1="23" x2="18" y2="14"/>
          </svg>
          dale@hervit7.example
        </li>
      </ul>

      <ul class="info-list credentials">
        <li class="info-item"><span class="cert-badge"></span>KPTB Certified Personal Trainer</li>
        <li class="info-item"><span class="cert-badge round"></span>CPR AED Northern Pulse Council</li>
        <li class="info-item"><span class="cert-badge"></span>B.A. Exercise Physiology W.L.M., 2004</li>
      </ul>
    </div>

    <div class="website-tab">www.hervit7.example</div>
  </div>
</body>
</html>
```